Holmvirke Cup (sports event site)

We are a sportsfederation with an event called Holmvirké Cup, which translates something like TeamPlay Cup. Co workers get together and play soccer, handball, running ect. for a weekend against other companies. The spirit is - for all to come and compete.

Basically the site objective is to present and sell the idea of gathering a few colleagues and comming to the event. The event consist of vairuos sports and a party on saturday night. Its an national event and we normally are 1.000-2.000 gathered to participate.

There should be an event page, and a standard page besides the frontpage
The event page is one page pr. sporttype on the event.

At the moment the event has an embeddes subsite on www.holmvirke-example.dk/cup, but we would like to make a small but visual great wordpress-ish site.

We have a logo and a visual style which you can se in the uploaded files.

It would be great if the design translates easily to wordpress, or even better delivers as an wordpress template for an extra payment.
Updates

Target Market(s)

Adults
Sports and healthinterested

Industry/Entity Type

Event

Number of Pages Required

3 page

Requirements
Must have
• Sign up (Tilmeld) buttons for the event and the newletter
• Resultsbutton pr. Event.
• Social media integration
• big pictures
• The event logo (Holmvirké Cup)
• The organisation logo (lysgrenmark)

```html
<!DOCTYPE html>
<html lang="da">
<head>
<meta charset="utf-8">
<title>Holmvirké Cup</title>
<link rel="stylesheet" href="https://fonts.googleapis.com/css2?family=Questrial&family=Lato:wght@400;700&display=swap">
<style>
:root{
  --navy:#0b2a55;
  --navy-deep:#082246;
  --blue:#1f77c0;
  --red:#d3232f;
  --yellow:#f0b21a;
  --grey-bg:#f2f2f2;
  --text:#333;
  --muted:#666;
  --white:#fff;
}
*{box-sizing:border-box;margin:0;padding:0}
html,body{width:1200px;height:2365px;overflow:hidden;background:var(--white)}
body{position:relative;font-family:"Lato",sans-serif;color:var(--text)}
.head{font-family:"Questrial",sans-serif}

.topbar{position:absolute;top:0;left:0;width:1200px;height:44px;background:var(--navy)}
.social{position:absolute;right:76px;top:7px;display:flex;gap:6px}
.social span{width:30px;height:30px;border:2px solid var(--white);border-radius:50%;display:block}

.hero{position:absolute;top:44px;left:0;width:1200px;height:689px;
  background:radial-gradient(ellipse at 50% 35%,#d9a58a 0,#c98a6d 12%,#2c6fc4 30%,#1d5aa8 55%,#7fa26a 85%,#a8b98d 100%)}
.site-header{position:absolute;top:44px;left:0;width:1200px;height:134px;background:rgba(255,255,255,.9)}
.brand{position:absolute;left:76px;top:-31px;width:116px;height:150px;text-align:center}
.brand-mark{width:96px;height:96px;margin:0 auto;border-radius:50%;background:var(--white);border:6px solid var(--blue)}
.brand-name{font-family:"Questrial",sans-serif;font-size:22px;color:var(--blue);line-height:1.05;margin-top:6px}
.nav{position:absolute;left:416px;top:58px;display:flex;gap:0}
.nav a{font-family:"Questrial",sans-serif;font-size:16px;color:#222;text-decoration:none;margin-right:38px;letter-spacing:.3px}
.btn{position:absolute;top:46px;height:44px;width:129px;color:var(--white);font-family:"Questrial",sans-serif;font-size:18px;display:flex;align-items:center;justify-content:center;border-radius:2px}
.btn-signup{left:859px;background:var(--red)}
.btn-event{left:997px;background:var(--yellow)}

.hero-band{position:absolute;top:563px;left:0;width:1200px;height:125px;background:rgba(225,237,250,.88);text-align:center;padding-top:20px}
.hero-band p{font-family:"Questrial",sans-serif;font-size:25px;color:#111;line-height:29px}
.hero-band .date{color:var(--blue);font-size:26px;font-weight:700;font-family:"Lato",sans-serif}

.sports{position:absolute;top:733px;left:0;width:1200px;height:478px;background:var(--grey-bg)}
.card{position:absolute;top:29px;width:243px;height:373px;background:var(--white);text-align:center}
.card .photo{width:243px;height:205px;border-bottom-left-radius:50% 60%;border-bottom-right-radius:50% 60%}
.card h3{font-family:"Questrial",sans-serif;font-weight:400;font-size:17px;margin-top:33px;color:#111}
.card p{font-size:13px;line-height:20px;color:#444;padding:0 22px;margin-top:14px}
.arrows{position:absolute;top:445px;left:563px;display:flex;gap:6px}
.arrows span{width:35px;height:33px;background:var(--white);display:flex;align-items:center;justify-content:center}

.intro{position:absolute;top:1211px;left:0;width:1200px;height:528px;text-align:center}
.intro h2{font-family:"Questrial",sans-serif;font-weight:400;font-size:16px;position:absolute;top:42px;width:100%}
.intro .date{position:absolute;top:58px;width:100%;font-size:28px;font-weight:700;color:var(--blue)}
.intro .lead{position:absolute;left:200px;width:800px;font-size:13.5px;line-height:20px;color:#444}
.col{position:absolute;top:262px;width:320px;text-align:center}
.col h4{font-family:"Questrial",sans-serif;font-weight:400;font-size:17px;line-height:21px;color:#111;height:52px}
.col p{font-size:13.5px;line-height:20px;color:#444;margin-top:8px;padding:0 30px}
.divider{position:absolute;top:265px;width:1px;height:215px;background:#ddd}

.why{position:absolute;top:1739px;left:0;width:766px;height:314px;background:var(--grey-bg)}
.why h3{position:absolute;left:74px;top:80px;font-family:"Questrial",sans-serif;font-weight:400;font-size:16px;color:#111}
.why ul{position:absolute;top:120px;list-style:none}
.why li{font-size:13.5px;color:#444;height:30px;display:flex;align-items:center;gap:10px}
.why-photo{position:absolute;top:1739px;left:766px;width:434px;height:314px;background:linear-gradient(180deg,#fafafa 0,#e8e8e8 30%,#2a66b8 60%,#1c4f96 100%)}

.footer{position:absolute;top:2053px;left:0;width:1200px;height:312px;background:var(--navy)}
.footer h5{font-family:"Lato",sans-serif;font-size:15px;font-weight:700;color:var(--white);position:absolute;top:42px}
.quick{position:absolute;left:73px;top:76px;list-style:none}
.quick li{font-size:12.5px;color:#c8d3e4;line-height:24px}
.partner{position:absolute;background:var(--white)}
.news-text{position:absolute;left:793px;top:74px;width:340px;font-size:12px;line-height:23px;color:#c8d3e4}
.field{position:absolute;left:793px;width:221px;height:37px;background:#f1f1f1;border-radius:4px;font-size:12.5px;color:#666;display:flex;align-items:center;gap:8px;padding-left:10px}
.signup{position:absolute;left:1025px;top:133px;width:101px;height:83px;background:var(--blue);border-radius:4px;color:var(--white);font-family:"Questrial",sans-serif;font-size:16px;display:flex;flex-direction:column;align-items:center;justify-content:center;gap:6px}
.footer-line{position:absolute;left:0;top:258px;width:1200px;height:1px;background:#23436e}
.copyright{position:absolute;top:276px;width:100%;text-align:center;font-size:12px;color:#9fb0c8}
</style>
</head>
<body>

<div class="topbar">
  <div class="social"><span></span><span></span><span></span><span></span><span></span></div>
</div>

<div class="hero" role="img" aria-label="Photo of smiling company sports participants in blue team shirts"></div>

<header class="site-header">
  <div class="brand">
    <div class="brand-mark"></div>
    <div class="brand-name">Holmvirké Cup</div>
  </div>
  <nav class="nav"><a>HOME</a><a>ABOUT US</a><a>EVENTS</a><a>CONTACT</a></nav>
  <div class="btn btn-signup">TILMELD</div>
  <div class="btn btn-event">PR. EVENT</div>
</header>

<div class="hero-band">
  <p>DANMARKS SJOVESTE FIRMAIDRÆTSFEST</p>
  <p>RAMMER STORKØBENHAVN</p>
  <p class="date">11.-13. SEPTEMBER 2015</p>
</div>

<section class="sports">
  <div class="card" style="left:74px">
    <div class="photo" role="img" aria-label="Photo of a badminton match in a sports hall" style="background:linear-gradient(160deg,#c9b79a,#7d6a55 50%,#2b3d7a)"></div>
    <h3>BADMINTON</h3>
    <p>Stil op til en venskabelig dyst henover nettet – eller kom og kæmp for firmaæren med ketsjer og fjerbold!</p>
  </div>
  <div class="card" style="left:344px">
    <div class="photo" role="img" aria-label="Photo of a player leaning over a billiard table" style="background:linear-gradient(160deg,#6e6e6e,#2a2a2a 50%,#1d6a3a)"></div>
    <h3>BILLARD</h3>
    <p>Er du en mester ved det grønne bord – eller spiller du billard for hyggens skyld? Begge slags billardfolk er velkomne!</p>
  </div>
  <div class="card" style="left:613px">
    <div class="photo" role="img" aria-label="Photo of a table tennis player in action" style="background:linear-gradient(160deg,#b07a4a,#8a5a34 45%,#3f8ec2)"></div>
    <h3>BORDTENNIS</h3>
    <p>Er du en garvet klubspiller, eller spiller du bare bordtennis engang imellem? Der er rækker for begge slags bat-mænd og -kvinder.</p>
  </div>
  <div class="card" style="left:883px">
    <div class="photo" role="img" aria-label="Photo of a handball player jumping to throw" style="background:linear-gradient(160deg,#2b2b2b,#c0582a 45%,#e0c23a)"></div>
    <h3>HÅNDBOLD</h3>
    <p>Saml både skarpskytterne og de hyggelige håndbold spillere til Holmvirké Cup.</p>
  </div>
  <div class="arrows">
    <span><svg width="12" height="10" viewBox="0 0 12 10"><path d="M11 5H1M5 1L1 5l4 4" stroke="#999" fill="none" stroke-width="1.4"/></svg></span>
    <span><svg width="12" height="10" viewBox="0 0 12 10"><path d="M1 5h10M7 1l4 4-4 4" stroke="#999" fill="none" stroke-width="1.4"/></svg></span>
  </div>
</section>

<section class="intro">
  <h2>HOLMVIRKÉ CUP I STORKØBENHAVN</h2>
  <div class="date">11.-13. SEPTEMBER 2015</div>
  <p class="lead" style="top:116px">Den anden weekend i september 2015 idrætsfester de danske arbejdspladser i Holmvang og omegn – og du og dine kolleger skal være med!</p>
  <p class="lead" style="top:178px">Til Holmvirké Cup får I en firmafest på den sunde og sjove måde. I tager afsted til en weekend pakket med idræt, aktiviteter, hygge og fællesskab – og kommer hjem med gode oplevelser med kollegerne i rygsækken.</p>

  <div class="col" style="left:90px">
    <h4>Vælg mellem 14 idrætsaktiviteter</h4>
    <p>Der er 14 forskellige idrætsaktiviteter at vælge mellem. Nogen for hold med flere personer og andre for enkeltpersoner. Nogen der giver masser af sved på panden og action, og andre der udfordrer hoved, teknik og logik.</p>
    <p style="margin-top:20px">Se alle aktiviteterne på de foregående sider – og læs mere på www.holmvirke-example.dk/cup</p>
  </div>
  <div class="divider" style="left:419px"></div>
  <div class="col" style="left:440px">
    <h4>Holmvang – weekendens primære samlingspunkt</h4>
    <p>De fleste af aktiviteterne foregår i og omkring Holmvanghallen – med et par afstikkere til bl.a. Roskilde.</p>
  </div>
  <div class="divider" style="left:779px"></div>
  <div class="col" style="left:800px">
    <h4>Fest lørdag aften</h4>
    <p>Lørdag aften samles alle deltagere i Holmvanghallen til stor fest med mad, livemusik, DJ og dans.</p>
  </div>
</section>

<section class="why">
  <h3>DERFOR SKAL I VÆRE MED</h3>
  <ul style="left:74px">
    <li><svg width="12" height="12" viewBox="0 0 12 12"><path d="M1 6l3.5 3.5L11 2" stroke="#999" fill="none" stroke-width="1.6"/></svg>Firmaidrætsfest på den sunde og sjove måde</li>
    <li><svg width="12" height="12" viewBox="0 0 12 12"><path d="M1 6l3.5 3.5L11 2" stroke="#999" fill="none" stroke-width="1.6"/></svg>Idræt hele weekenden – fest lørdag aften</li>
    <li><svg width="12" height="12" viewBox="0 0 12 12"><path d="M1 6l3.5 3.5L11 2" stroke="#999" fill="none" stroke-width="1.6"/></svg>Frit valg mellem 14 forskellige idrætsaktiviteter</li>
    <li><svg width="12" height="12" viewBox="0 0 12 12"><path d="M1 6l3.5 3.5L11 2" stroke="#999" fill="none" stroke-width="1.6"/></svg>Et idrætsstævne med hyggegaranti</li>
  </ul>
  <ul style="left:419px">
    <li><svg width="12" height="12" viewBox="0 0 12 12"><path d="M1 6l3.5 3.5L11 2" stroke="#999" fill="none" stroke-width="1.6"/></svg>Deltagere fra arbejdspladser fra hele Danmark</li>
    <li><svg width="12" height="12" viewBox="0 0 12 12"><path d="M1 6l3.5 3.5L11 2" stroke="#999" fill="none" stroke-width="1.6"/></svg>Stor fest i Holmvanghallen</li>
    <li><svg width="12" height="12" viewBox="0 0 12 12"><path d="M1 6l3.5 3.5L11 2" stroke="#999" fill="none" stroke-width="1.6"/></svg>Overnatning på skole, camping eller hotel</li>
    <li><svg width="12" height="12" viewBox="0 0 12 12"><path d="M1 6l3.5 3.5L11 2" stroke="#999" fill="none" stroke-width="1.6"/></svg>Alle kan deltage</li>
  </ul>
</section>
<div class="why-photo" role="img" aria-label="Photo of a team of colleagues in blue shirts with arms around each other"></div>

<footer class="footer">
  <h5 style="left:73px">Quick Links</h5>
  <ul class="quick"><li>Home</li><li>About Us</li><li>Events</li><li>Contact</li></ul>

  <h5 style="left:255px">Samarbejdspartner</h5>
  <div class="partner" style="left:255px;top:85px;width:96px;height:96px;border-radius:6px"></div>

  <h5 style="left:524px">Samarbejdspartner</h5>
  <div class="partner" style="left:524px;top:84px;width:206px;height:58px;border-radius:29px"></div>
  <div class="partner" style="left:524px;top:159px;width:206px;height:58px;border-radius:29px"></div>

  <h5 style="left:793px">Newsletter Sign Up - Today!!!</h5>
  <p class="news-text">Enter your name and email to subscribe or unsubscribe to our newsletters and receive latest offers!!!..</p>
  <div class="field" style="top:134px"><svg width="14" height="14" viewBox="0 0 14 14"><circle cx="7" cy="4.5" r="3.2" fill="#1f77c0"/><path d="M1 14c0-4 3-6 6-6s6 2 6 6z" fill="#1f77c0"/></svg>Enter Your Name</div>
  <div class="field" style="top:180px"><svg width="14" height="12" viewBox="0 0 14 12"><rect x="1" y="2" width="12" height="9" rx="1" fill="none" stroke="#1f77c0" stroke-width="1.5"/><path d="M1 3l6 4 6-4" stroke="#1f77c0" fill="none" stroke-width="1.5"/></svg>Enter Your Email</div>
  <div class="signup"><svg width="26" height="24" viewBox="0 0 26 24"><path d="M1 11L25 1 20 23 13 16z" fill="#fff"/><path d="M13 16l12-15" stroke="#1f77c0" stroke-width="1.5"/></svg>SIGN UP</div>

  <div class="footer-line"></div>
  <p class="copyright">© 2015 Holmvirké Cup All rights reserved. &nbsp;|&nbsp; Privacy Policy &nbsp;|&nbsp; Site Map</p>
</footer>

</body>
</html>
```